Plumbing & Heating company

A leaflet containing -

Company name - Brackenfold Plumbing Solutions
logo
Mobile number - 07700 914226
Landline - 01632 870512
Email - Info@brackenfoldplumbing.example.co.uk
website - Brackenfold-plumbing.example.co.uk
Social media logos - pixgram, Chatterly

services we offer

- Boiler replacements (free quote)
- General plumbing & heating
- Tap replacements
- 1st & 2nd
- New builds & Extensions
- Cylinder replcemets

```html
<!DOCTYPE html>
<html lang="en">
<head>
<meta charset="utf-8">
<title>Brackenfold Plumbing Solutions – Leaflet</title>
<link rel="stylesheet" href="https://fonts.googleapis.com/css2?family=Oswald:wght@500;600;700&family=Montserrat:wght@600;700;800&display=swap">
<style>
  :root {
    --stage: #666666;
    --paper: #ffffff;
    --orange: #fa9a28;
    --blue: #0a88c9;
    --ink: #1d1d1f;
    --black: #202020;
    --white: #ffffff;
  }
  * { margin: 0; padding: 0; box-sizing: border-box; }
  html, body { width: 1200px; height: 1001px; overflow: hidden; background: var(--stage); }
  .leaflet {
    position: absolute; left: 274px; top: 79px;
    width: 652px; height: 842px; background: var(--paper); overflow: hidden;
  }
  .leaflet-shapes { position: absolute; inset: 0; }
  .brand {
    position: absolute; left: 34px; top: 56px; width: 220px;
    display: flex; align-items: center; gap: 8px;
    font-family: "Montserrat", sans-serif; font-weight: 800; color: var(--blue);
  }
  .brand-dot { width: 16px; height: 16px; border-radius: 50%; background: var(--orange); flex: none; }
  .brand-name { font-size: 17px; line-height: 1.15; letter-spacing: .5px; text-transform: uppercase; }
  .brand-name small { display: block; font-size: 11px; letter-spacing: 1.6px; font-weight: 800; }
  .hero-title {
    position: absolute; left: 43px; top: 176px; color: var(--white);
    font-family: "Oswald", sans-serif; font-weight: 700; text-transform: uppercase;
  }
  .hero-title .name { display: block; font-size: 74px; line-height: 1; letter-spacing: -1px; transform: scaleX(.78); transform-origin: left; }
  .hero-title .trade { display: block; font-size: 42px; line-height: 1; font-weight: 600; margin-top: 14px; transform: scaleX(.8); transform-origin: left; }
  .hero-intro {
    position: absolute; left: 44px; top: 336px; width: 330px; color: var(--white);
    font-family: "Montserrat", sans-serif; font-weight: 700; font-size: 11.6px; line-height: 17.7px; text-transform: uppercase;
  }
  .services-heading {
    position: absolute; left: 291px; top: 485px; width: 361px; text-align: center;
    font-family: "Montserrat", sans-serif; font-weight: 800; font-size: 24px; color: var(--white); letter-spacing: .5px;
  }
  .services-list { position: absolute; left: 301px; top: 528px; list-style: none; }
  .services-list li {
    display: flex; align-items: center; gap: 8px; height: 38.3px;
    font-family: "Oswald", sans-serif; font-weight: 600; font-size: 24px; color: var(--ink); text-transform: uppercase;
  }
  .services-list li span { display: inline-block; transform: scaleX(.82); transform-origin: left; white-space: nowrap; }
  .services-list svg { width: 19px; height: 19px; flex: none; }
  .contact {
    position: absolute; font-family: "Montserrat", sans-serif; font-weight: 600; color: var(--white);
    display: flex; align-items: center; gap: 6px; white-space: nowrap;
  }
  .contact svg { width: 9px; height: 9px; flex: none; }
  .contact.phone { font-size: 12px; left: 36px; }
  .contact.web { font-size: 10px; left: 170px; }
  .contact.social { font-size: 10px; left: 427px; font-weight: 600; }
  .contact.social .icon { width: 14px; height: 14px; border-radius: 50%; background: var(--white); flex: none; }
</style>
</head>
<body>
<main class="leaflet">
  <svg class="leaflet-shapes" viewBox="0 0 652 842" width="652" height="842">
    <!-- hero photo with orange frame -->
    <polygon points="250,0 652,0 652,462 322,462" fill="var(--orange)"/>
    <polygon role="img" aria-label="Photo: installed boiler and hot water cylinder with copper pipework" points="263,0 652,0 652,448 330,448" fill="#cfcdc8"/>
    <!-- main orange panel -->
    <polygon points="0,166 377,166 417,421 0,421" fill="var(--orange)"/>
    <!-- small photo frames -->
    <polygon points="0,452 181,452 203,594 0,594" fill="var(--orange)"/>
    <polygon role="img" aria-label="Photo: boiler, manifold pipework and cylinder on a dark wall" points="0,461 175,461 193,587 0,587" fill="#8a7a68"/>
    <polygon points="0,606 181,606 203,747 0,747" fill="var(--orange)"/>
    <polygon role="img" aria-label="Photo: copper pipe runs laid across floor joists" points="0,615 175,615 193,740 0,740" fill="#a98a6e"/>
    <!-- services heading band -->
    <polygon points="291,485 652,485 652,518 295,518" fill="var(--blue)"/>
    <!-- footer -->
    <polygon points="0,764 405,764 417,842 0,842" fill="var(--blue)"/>
    <polygon points="406,772 652,772 652,842 417,842" fill="var(--black)"/>
  </svg>

  <div class="brand">
    <span class="brand-dot"></span>
    <div class="brand-name">Brackenfold<small>Plumbing Solutions</small></div>
  </div>

  <h1 class="hero-title">
    <span class="name">Brackenfold</span>
    <span class="trade">Plumbing Solutions</span>
  </h1>
  <p class="hero-intro">Are a young and ambitious plumbing &amp; heating company with close to a decade of experience.</p>

  <h2 class="services-heading">OUR SERVICES</h2>
  <ul class="services-list">
    <li><svg viewBox="0 0 20 20"><circle cx="9" cy="11" r="7.5" fill="none" stroke="var(--blue)" stroke-width="2.2"/><path d="M5 10.5l3.5 3.5L18 3" fill="none" stroke="var(--blue)" stroke-width="2.6" stroke-linecap="round"/></svg><span>Boiler replacements &nbsp;(free quote)</span></li>
    <li><svg viewBox="0 0 20 20"><circle cx="9" cy="11" r="7.5" fill="none" stroke="var(--blue)" stroke-width="2.2"/><path d="M5 10.5l3.5 3.5L18 3" fill="none" stroke="var(--blue)" stroke-width="2.6" stroke-linecap="round"/></svg><span>General plumbing &amp; heating</span></li>
    <li><svg viewBox="0 0 20 20"><circle cx="9" cy="11" r="7.5" fill="none" stroke="var(--blue)" stroke-width="2.2"/><path d="M5 10.5l3.5 3.5L18 3" fill="none" stroke="var(--blue)" stroke-width="2.6" stroke-linecap="round"/></svg><span>Tap replacements</span></li>
    <li><svg viewBox="0 0 20 20"><circle cx="9" cy="11" r="7.5" fill="none" stroke="var(--blue)" stroke-width="2.2"/><path d="M5 10.5l3.5 3.5L18 3" fill="none" stroke="var(--blue)" stroke-width="2.6" stroke-linecap="round"/></svg><span>1st &amp; 2nd</span></li>
    <li><svg viewBox="0 0 20 20"><circle cx="9" cy="11" r="7.5" fill="none" stroke="var(--blue)" stroke-width="2.2"/><path d="M5 10.5l3.5 3.5L18 3" fill="none" stroke="var(--blue)" stroke-width="2.6" stroke-linecap="round"/></svg><span>New builds &amp; extensions</span></li>
    <li><svg viewBox="0 0 20 20"><circle cx="9" cy="11" r="7.5" fill="none" stroke="var(--blue)" stroke-width="2.2"/><path d="M5 10.5l3.5 3.5L18 3" fill="none" stroke="var(--blue)" stroke-width="2.6" stroke-linecap="round"/></svg><span>Cylinder replcemets</span></li>
  </ul>

  <div class="contact phone" style="top:785px"><svg viewBox="0 0 10 10"><rect x="2.5" y="0.5" width="5" height="9" rx="1" fill="none" stroke="var(--white)" stroke-width="1.2"/></svg>07700 914226</div>
  <div class="contact phone" style="top:811px"><svg viewBox="0 0 10 10"><path d="M2 1l2 2-1 1.5c.8 1.3 1.7 2.2 3 3L7.5 6l2 2-1.5 1.5C4.5 9 1 5.5.5 2z" fill="var(--white)"/></svg>01632 870512</div>
  <div class="contact web" style="top:787px"><svg viewBox="0 0 10 10"><rect x="0.5" y="2" width="9" height="6" fill="var(--white)"/><path d="M.5 2l4.5 3.5L9.5 2" fill="none" stroke="var(--blue)" stroke-width="1"/></svg>Info@brackenfoldplumbing.example.co.uk</div>
  <div class="contact web" style="top:813px"><svg viewBox="0 0 10 10"><path d="M2 1l6 4.5-3 .5 1.5 3-1 .5L4 6.5 2 8.5z" fill="var(--white)"/></svg>Brackenfold-plumbing.example.co.uk</div>
  <div class="contact social" style="top:789px"><span class="icon"></span>@Brackenfoldplumbingsolutions</div>
  <div class="contact social" style="top:815px"><span class="icon"></span>/Brackenfoldplumbingsolutions</div>
</main>
</body>
</html>
```